Packaging Design Project

Hi,

We are an small SME active in the hotels industry.
We deliver guest amenities.

We are thinking to create a our first neutral range for accessories.
This consists of a box (94mm/75mm/75mm) in which accessories will be stored.
Here below, you will find an editable pdf with the dimensions of the box.

This is for a neutral range supposed to fit in diverse kind of room, please take this into account : no vivid colors, you can imagine logo and/or colors as far as it remains discrete.

The box should be mostly white. You can imagine logo, forms, frames ... as fas as more than 60% of the box is white.

We will be very reactive to give you feedback. In the same time, you can propose a name for this neutral range.

In order to know the kind of name we like, our other range (not accessories) are called : Brio, Calm, Fresh Drift, Everyday.

For info, a range is composed by : soap, shower gel, body lotion...
the accessories of a range is composed by : shower cap, shoe sponge, sewing kit ...

Thanks in advance for your work !

Target Market(s)

it's a B2B hotels environment, but our client range from 1* to 5*

Industry/Entity Type

Industry

Requirements
Must have
• You have to respect the scale of the box provided in the file below.
Somewhere should appear our website : www.plorvane.be but in a very discrete way.

The design should be in black & white or gray & white
Nice to have
• a small discrete logo somewhere, but this is not mandatory
Should not have
• a lot of colors, a design having a too strong identity. this design is supposed to fit with the design of the hotel, whatever it is.

```html
<!DOCTYPE html>
<html lang="en">
<head>
<meta charset="utf-8">
<title>Neutral Accessories Range – Packaging</title>
<link rel="stylesheet" href="https://fonts.googleapis.com/css2?family=Bungee&family=Bungee+Outline&family=Open+Sans:wght@400&display=swap">
<style>
  :root {
    --ink: #5f5f5f;
    --ink-light: #8a8a8a;
    --frame: #222222;
    --paper: #ffffff;
  }
  * { margin: 0; padding: 0; box-sizing: border-box; }
  html, body {
    width: 1200px;
    height: 1200px;
    overflow: hidden;
    background: var(--paper);
  }
  .board {
    position: relative;
    width: 1200px;
    height: 1200px;
    background: var(--paper);
  }
  .wordmark {
    position: absolute;
    left: 44px;
    font-family: "Bungee", sans-serif;
    font-size: 132px;
    line-height: 1;
    letter-spacing: 4px;
    color: var(--ink);
  }
  .wordmark--primary { top: 270px; }
  .wordmark--secondary { top: 462px; color: var(--ink-light); }

  .panel {
    position: absolute;
    top: 805px;
    width: 262px;
    height: 331px;
    border: 1.5px solid var(--frame);
    background: var(--paper);
  }
  .panel--front { left: 46px; }
  .panel--side-a { left: 327px; }
  .panel--back { left: 607px; }
  .panel--side-b { left: 886px; }

  .panel__name {
    position: absolute;
    left: 8px;
    bottom: 14px;
    font-family: "Bungee", sans-serif;
    font-size: 74px;
    line-height: 1;
    letter-spacing: 1px;
    color: var(--ink);
  }
  .panel__contents {
    position: absolute;
    left: 9px;
    font-family: "Bungee Outline", sans-serif;
    font-size: 18px;
    line-height: 24px;
    color: var(--ink);
    white-space: nowrap;
  }
  .panel--front .panel__contents { top: 128px; }
  .panel--side-b .panel__contents { top: 108px; left: 9px; }

  .panel__contents--vertical {
    position: absolute;
    top: 6px;
    right: 6px;
    font-family: "Bungee Outline", sans-serif;
    font-size: 18px;
    line-height: 22px;
    color: var(--ink);
    writing-mode: vertical-rl;
    transform: rotate(180deg);
    white-space: nowrap;
  }
  .panel__web {
    position: absolute;
    top: 157px;
    left: 0;
    width: 100%;
    text-align: center;
    font-family: "Open Sans", sans-serif;
    font-size: 11px;
    color: #333333;
  }
</style>
</head>
<body>
<main class="board">
  <div class="wordmark wordmark--primary">pack</div>
  <div class="wordmark wordmark--secondary">pack</div>

  <section class="panel panel--front">
    <p class="panel__contents">shower<br>body lotion</p>
    <div class="panel__name">pack</div>
  </section>

  <section class="panel panel--side-a">
    <p class="panel__contents--vertical">soap<br>gel</p>
    <div class="panel__name">pack</div>
  </section>

  <section class="panel panel--back">
    <p class="panel__web">www.plorvane.be</p>
    <div class="panel__name">pack</div>
  </section>

  <section class="panel panel--side-b">
    <p class="panel__contents">shower cap<br>shoe sponge<br>sewing kit</p>
    <div class="panel__name">pack</div>
  </section>
</main>
</body>
</html>
```